Business cards for veterinary clinic

Hi, We are looking for business cards to be designed for our other veterinary clinic. We were very happy with the design done for our other clinic a few months ago. We already have a logo for use which I will attach (please use the image not the text around.
We need a couple of different cards (same design with different names on them) produced

Industry/Entity Type

Veterinary

Contact Information for Business Card

Mossvale Creek Vet Clinic
58 Orchard Rd
Ashbury Glen
VIC 3571
03) 5812 4396
clinic@mossvalecreekvetclinic.com.au

Font styles to use
Sans Serif

Colors
0455a3
0592cd

Requirements
Must have
• Three different names
• 1. Generic (no name) with email clinic@mossvalecreekvetclinic.com.au
• 2. Leonie Pratt -Director with email leonie@mossvalecreekvetclinic.com.au
• 3. Declan Hume - Vet Director with email leonie@mossvalecreekvetclinic.com.au

```html
<!DOCTYPE html>
<html lang="en">
<head>
<meta charset="utf-8">
<title>Mossvale Creek Vet Clinic – Business Cards</title>
<link rel="stylesheet" href="https://fonts.googleapis.com/css2?family=Lato:wght@300;400;700;900&display=swap">
<style>
  :root {
    --backdrop: #2a2a2c;
    --navy: #0455a3;
    --navy-deep: #034a8e;
    --sky: #0592cd;
    --sky-soft: #4db3d6;
    --white: #ffffff;
    --paper: #f4f6f8;
    --ink-light: #d9ecf8;
  }
  * { box-sizing: border-box; margin: 0; padding: 0; }
  html, body {
    width: 1200px; height: 997px; overflow: hidden;
    background: var(--backdrop);
    font-family: "Lato", Arial, sans-serif;
  }
  .canvas { position: relative; width: 1200px; height: 997px; }

  .card {
    position: absolute; width: 540px; height: 330px;
    border-radius: 18px; overflow: hidden;
    box-shadow: 0 14px 30px rgba(0,0,0,.45);
  }

  /* ---------- Back card ---------- */
  .card--back { left: 70px; top: 150px; background: linear-gradient(180deg, var(--sky) 0%, #1585bd 100%); }
  .back-band {
    position: absolute; left: 0; right: 0; top: 92px; height: 146px;
    background: linear-gradient(180deg, var(--white), var(--paper));
  }
  .back-text { position: absolute; left: 28px; top: 122px; width: 330px; white-space: nowrap; }
  .tagline { font-size: 12px; font-weight: 300; letter-spacing: .6px; color: var(--sky); text-transform: uppercase; }
  .tagline strong { font-weight: 400; }
  .back-name { margin-top: 8px; font-size: 20px; font-weight: 300; color: var(--sky-soft); line-height: 1.1; }
  .back-name strong { font-weight: 400; color: var(--sky); }
  .back-web { margin-top: 10px; font-size: 12px; color: var(--navy); }

  .logo-seal {
    position: absolute; border-radius: 50%;
    display: flex; align-items: center; justify-content: center; text-align: center;
    background: var(--white); border: 5px solid var(--sky);
  }
  .logo-seal__name { font-weight: 700; color: var(--sky); line-height: 1.2; }
  .card--back .logo-seal { left: 356px; top: 76px; width: 166px; height: 166px; }
  .card--back .logo-seal__name { font-size: 16px; }

  /* ---------- Front card ---------- */
  .card--front { left: 590px; top: 500px; background: var(--paper); }
  .front-shape { position: absolute; inset: 0; }
  .card--front .logo-seal { left: 36px; top: 90px; width: 180px; height: 150px; border-color: var(--navy); }
  .card--front .logo-seal__name { font-size: 16px; color: var(--navy); }

  .front-info { position: absolute; left: 300px; right: 20px; top: 32px; color: var(--white); white-space: nowrap; }
  .person { display: flex; align-items: baseline; justify-content: space-between; }
  .person__name { font-size: 19px; font-weight: 300; letter-spacing: .5px; }
  .person__name strong { font-weight: 400; }
  .person__role { font-size: 10.5px; font-weight: 700; }
  .person__email { font-size: 10.5px; font-weight: 700; margin-top: 4px; }

  .clinic-name { margin-top: 30px; font-size: 16px; font-weight: 300; color: var(--ink-light); }
  .clinic-name strong { font-weight: 400; color: var(--white); }

  .contact-list { list-style: none; margin-top: 12px; }
  .contact-list li {
    display: flex; align-items: center; justify-content: flex-end; gap: 8px;
    font-size: 11px; font-weight: 700; height: 20px;
  }
  .contact-list svg { width: 13px; height: 13px; fill: var(--white); flex: none; }
  .address { margin-top: 12px; font-size: 10.5px; font-weight: 700; line-height: 1.6; }
</style>
</head>
<body>
<main class="canvas">

  <section class="card card--back" aria-label="Business card back">
    <div class="back-band"></div>
    <div class="back-text">
      <p class="tagline">All of your <strong>veterinary needs</strong></p>
      <p class="back-name">Mossvale Creek <strong>Veterinary Clinic</strong></p>
      <p class="back-web">www.<strong>mossvalecreekvetclinic</strong>.com.au</p>
    </div>
    <div class="logo-seal"><span class="logo-seal__name">Mossvale Creek<br>Vet Clinic</span></div>
  </section>

  <section class="card card--front" aria-label="Business card front">
    <svg class="front-shape" viewBox="0 0 540 330" preserveAspectRatio="none" aria-hidden="true">
      <defs>
        <linearGradient id="frontBlue" x1="0" y1="0" x2="1" y2="1">
          <stop offset="0" stop-color="#0a68b3"/>
          <stop offset="1" stop-color="#034a8e"/>
        </linearGradient>
      </defs>
      <path d="M240 0 Q330 165 262 330 L540 330 L540 0 Z" fill="#4db3d6"/>
      <path d="M256 0 Q348 165 280 330 L540 330 L540 0 Z" fill="url(#frontBlue)"/>
    </svg>
    <div class="logo-seal"><span class="logo-seal__name">Mossvale Creek<br>Vet Clinic</span></div>

    <div class="front-info">
      <div class="person">
        <span class="person__name">DECLAN <strong>HUME</strong></span>
        <span class="person__role">Vet Director</span>
      </div>
      <p class="person__email">leonie@mossvalecreekvetclinic.com.au</p>

      <p class="clinic-name">Mossvale Creek <strong>Veterinary Clinic</strong></p>

      <ul class="contact-list">
        <li>(03) 5812 4396
          <svg viewBox="0 0 24 24" aria-hidden="true"><path d="M6.6 10.8a15 15 0 006.6 6.6l2.2-2.2a1 1 0 011-.25 11.4 11.4 0 003.6.57 1 1 0 011 1V20a1 1 0 01-1 1A17 17 0 013 4a1 1 0 011-1h3.5a1 1 0 011 1c0 1.25.2 2.45.57 3.57a1 1 0 01-.25 1z"/></svg>
        </li>
        <li>mossvalecreekvetclinic.com.au
          <svg viewBox="0 0 24 24" aria-hidden="true"><path d="M2 5h20v14H2z M4 7v.5l8 5 8-5V7z" fill-rule="evenodd"/></svg>
        </li>
        <li>
          <svg viewBox="0 0 24 24" aria-hidden="true"><path d="M12 3l10 9h-3v8h-5v-6h-4v6H5v-8H2z"/></svg>
        </li>
      </ul>

      <p class="address">clinic@mossvalecreekvetclinic.com.au<br>58 Orchard Rd Ashbury Glen VIC 3571</p>
    </div>
  </section>

</main>
</body>
</html>
```